Wine label design for my wife. Wine called "The Mirabel"

I need a wine label face lift of one of my premium wines in my collection. My wine sells in Harbor Lark's all over the States. My current label is called The Mirabel (my wife's name) and the illustration of her eyes is done by a well know artist from South Africa. I do not have to use this illustration and therefor I attached several pictures of her and her eyes, even when she was a little girl. The wine's also made in South Africa. This is a premium wine that we only sell 2000 bottles per year. The wine sells at 60 usd per bottle, The current label is too white. I also think her eyes should look more at the person buying it, than away from them.

Target Market(s)

Top end wine buyers

Font styles to use
Decorative
Script

Requirements
Must have
• 'The Mirabel' must be on the label
An illustration must be on the label
Basically all the info that's on the current label must be on by law. As per Sample
Nice to have
• Maybe some ideas of her whole face?
Should not have
• any gold colour

```html
<!DOCTYPE html>
<html lang="en">
<head>
<meta charset="utf-8">
<title>The Mirabel – Sauvignon Blanc Label</title>
<link rel="stylesheet" href="https://fonts.googleapis.com/css2?family=Pinyon+Script&family=Cormorant+Garamond:ital,wght@0,500;0,600;1,500&display=swap">
<style>
  :root {
    --backdrop: #b9b9b9;
    --label-black: #0b0b0b;
    --label-edge: #1c1c1c;
    --band-light: #5a5a5a;
    --silver: #dcdcdc;
    --silver-deep: #9c9c9c;
    --ivory: #f1efea;
    --portrait-light: #cfcfcf;
    --portrait-dark: #7a7a7a;
  }
  * { margin: 0; padding: 0; box-sizing: border-box; }
  html, body {
    width: 1200px;
    height: 857px;
    overflow: hidden;
    background: var(--backdrop);
  }
  .canvas {
    position: relative;
    width: 1200px;
    height: 857px;
  }
  .label {
    position: absolute;
    left: 150px;
    top: 121px;
    width: 900px;
    height: 614px;
    background: radial-gradient(ellipse at 50% 45%, var(--label-edge) 0%, var(--label-black) 70%);
    color: var(--ivory);
    text-align: center;
    overflow: hidden;
  }
  .label__band {
    position: absolute;
    left: 0;
    right: 0;
    height: 26px;
    background: linear-gradient(180deg, transparent 0%, var(--band-light) 50%, transparent 100%);
  }
  .label__band--top { top: 14px; opacity: 0.55; }
  .label__band--bottom { bottom: 14px; opacity: 0.4; }
  .label__name {
    position: absolute;
    top: 78px;
    left: 0;
    right: 0;
    font-family: "Pinyon Script", cursive;
    font-weight: 400;
    font-size: 88px;
    line-height: 1;
    color: var(--silver);
  }
  .label__variety {
    position: absolute;
    top: 190px;
    left: 0;
    right: 0;
    font-family: "Cormorant Garamond", serif;
    font-weight: 500;
    font-size: 34px;
    line-height: 1.2;
    letter-spacing: 1px;
    color: var(--silver);
  }
  .label__since {
    position: absolute;
    top: 232px;
    left: 0;
    right: 0;
    display: flex;
    justify-content: center;
    align-items: center;
    gap: 14px;
    font-family: "Cormorant Garamond", serif;
    font-style: italic;
    font-weight: 500;
    font-size: 28px;
    line-height: 1.2;
    color: var(--silver);
  }
  .label__rule {
    width: 90px;
    height: 2px;
    background: var(--silver-deep);
  }
  .label__portrait {
    position: absolute;
    left: 183px;
    top: 310px;
    width: 534px;
    height: 150px;
    background: linear-gradient(90deg, var(--portrait-dark) 0%, var(--portrait-light) 30%, var(--portrait-light) 70%, var(--portrait-dark) 100%);
  }
  .label__winery {
    position: absolute;
    top: 494px;
    left: 0;
    right: 0;
    font-family: "Cormorant Garamond", serif;
    font-weight: 600;
    font-size: 30px;
    line-height: 1.2;
    color: var(--ivory);
  }
  .label__divider {
    position: absolute;
    top: 542px;
    left: 50%;
    transform: translateX(-50%);
  }
  .label__origin {
    position: absolute;
    top: 564px;
    left: 0;
    right: 0;
    font-family: "Cormorant Garamond", serif;
    font-weight: 600;
    font-size: 16px;
    line-height: 1.2;
    letter-spacing: 5px;
    color: var(--ivory);
  }
</style>
</head>
<body>
  <main class="canvas">
    <section class="label" aria-label="Wine label">
      <div class="label__band label__band--top"></div>
      <h1 class="label__name">The Mirabel</h1>
      <p class="label__variety">SAUVIGNON BLANC</p>
      <p class="label__since"><span class="label__rule"></span>Since 2017<span class="label__rule"></span></p>
      <div class="label__portrait" role="img" aria-label="Black and white illustration of a woman's eyes"></div>
      <p class="label__winery">ROWAN ASHBY WINES</p>
      <svg class="label__divider" width="110" height="10" viewBox="0 0 110 10" aria-hidden="true">
        <line x1="0" y1="5" x2="48" y2="5" stroke="var(--silver-deep)" stroke-width="1.5"/>
        <rect x="51" y="1" width="8" height="8" transform="rotate(45 55 5)" fill="var(--silver-deep)"/>
        <line x1="62" y1="5" x2="110" y2="5" stroke="var(--silver-deep)" stroke-width="1.5"/>
      </svg>
      <p class="label__origin">SOUTH AFRICA</p>
      <div class="label__band label__band--bottom"></div>
    </section>
  </main>
</body>
</html>
```